Ward Compass Business Card Design*

We need a business card design for our company Ward Compass. Our company is specialized in providing online consulting services regarding medical institutions, hospitals and doctors. We work with patients worldwide looking to choose between healthcare providers. We have a website you may use as a reference, where we list doctors and clinics worldwide. So we target Medical providers as well as patients worldwide.
Target Market(s)
Medical Providers and patients around the world
Industry/Entity Type
Medical
Contact Information for Business Card
Salma Derkaoui
CEO
+90 612 348 2071
info@wardcompass-example.com
www.wardcompass-example.com
14 Annakhil 3 H.R.B. Rabat, Morocco
Requirements
Must have
- Company logo/name on one full side, personal info and smaller logo and company name on the other side.
Nice to have
- Smart and elegant design

```html
<!DOCTYPE html>
<html lang="en">
<head>
<meta charset="utf-8">
<title>Ward Compass – Business Card</title>
<link href="https://fonts.googleapis.com/css2?family=Montserrat:wght@600&family=Roboto:wght@400;500;700&display=swap" rel="stylesheet">
<style>
  :root {
    --navy: #143865;
    --grey: #7d7d7d;
    --white: #ffffff;
    --backdrop: #3b3f45;
  }
  * { margin: 0; padding: 0; box-sizing: border-box; }
  html, body {
    width: 1200px; height: 1000px; overflow: hidden;
    background: var(--backdrop);
  }
  .canvas {
    position: relative; width: 1200px; height: 1000px;
  }
  .card {
    position: absolute; left: 220px; width: 760px; height: 434px;
    box-shadow: 0 10px 30px rgba(0,0,0,0.45);
    overflow: hidden;
  }
  /* Brand side */
  .card--brand { top: 46px; background: var(--navy); }
  .brand-lockup {
    position: absolute; inset: 0;
    display: flex; align-items: center; justify-content: center; gap: 22px;
  }
  .brand-dot {
    width: 64px; height: 64px; border-radius: 50%;
    background: var(--white);
  }
  .brand-name {
    font-family: "Montserrat", sans-serif; font-weight: 600;
    font-size: 52px; letter-spacing: 1px; color: var(--white);
    text-transform: uppercase;
  }
  /* Contact side */
  .card--contact { top: 520px; background: var(--white); }
  .contact-lockup {
    position: absolute; top: 70px; left: 0; right: 0;
    display: flex; align-items: center; justify-content: center; gap: 16px;
  }
  .contact-lockup .brand-dot { width: 40px; height: 40px; background: var(--navy); }
  .contact-lockup .brand-name { font-size: 36px; color: var(--navy); }
  .person {
    position: absolute; top: 215px; right: 420px; text-align: right;
    font-family: "Roboto", sans-serif; font-weight: 700;
  }
  .person-name { font-size: 22px; color: var(--navy); letter-spacing: 0.5px; }
  .person-role { font-size: 19px; color: var(--grey); margin-top: 10px; }
  .divider {
    position: absolute; left: 370px; top: 205px; width: 2px; height: 120px;
    background: var(--navy);
  }
  .details {
    position: absolute; left: 392px; top: 200px;
    font-family: "Roboto", sans-serif; font-size: 16px; color: var(--grey);
    list-style: none; line-height: 1.35;
  }
  .details li { display: flex; align-items: center; gap: 8px; margin-bottom: 6px; }
  .details .address { display: block; padding-left: 22px; }
  .details svg { width: 14px; height: 14px; flex: none; fill: var(--navy); }
  .details .web { color: var(--navy); }
  .rule {
    position: absolute; left: 0; right: 0; top: 354px; height: 3px;
    background: var(--grey);
  }
  .band {
    position: absolute; left: 0; right: 0; top: 366px; bottom: 0;
    background: var(--navy);
  }
</style>
</head>
<body>
<main class="canvas">
  <section class="card card--brand">
    <div class="brand-lockup">
      <span class="brand-dot"></span>
      <span class="brand-name">Ward Compass</span>
    </div>
  </section>

  <section class="card card--contact">
    <div class="contact-lockup">
      <span class="brand-dot"></span>
      <span class="brand-name">Ward Compass</span>
    </div>

    <div class="person">
      <p class="person-name">SALMA DERKAOUI</p>
      <p class="person-role">CEO</p>
    </div>

    <div class="divider"></div>

    <ul class="details">
      <li class="address">14 Annakhil 3 H.R.B.<br>Rabat, Morocco</li>
      <li>
        <svg viewBox="0 0 24 24" aria-hidden="true"><path d="M6.6 10.8a15.1 15.1 0 0 0 6.6 6.6l2.2-2.2a1 1 0 0 1 1-.25 11.4 11.4 0 0 0 3.6.57 1 1 0 0 1 1 1V20a1 1 0 0 1-1 1A17 17 0 0 1 3 4a1 1 0 0 1 1-1h3.5a1 1 0 0 1 1 1c0 1.25.2 2.45.57 3.57a1 1 0 0 1-.25 1z"/></svg>
        +90 612 348 2071
      </li>
      <li>
        <svg viewBox="0 0 24 24" aria-hidden="true"><path d="M2 5h20v14H2zm2 2v.5l8 5 8-5V7zm0 2.8V17h16V9.8l-8 5z"/></svg>
        info@wardcompass-example.com
      </li>
      <li class="web">
        <svg viewBox="0 0 24 24" aria-hidden="true"><path d="M12 2a10 10 0 1 0 0 20 10 10 0 0 0 0-20zm0 2a8 8 0 0 1 7.7 6H16a12 12 0 0 0-2-5.7A8 8 0 0 1 12 4zm-2 .3A12 12 0 0 0 8 10H4.3A8 8 0 0 1 10 4.3zM4.3 14H8a12 12 0 0 0 2 5.7A8 8 0 0 1 4.3 14zM10 10a10 10 0 0 1 2-5 10 10 0 0 1 2 5zm0 4h4a10 10 0 0 1-2 5 10 10 0 0 1-2-5zm4 5.7a12 12 0 0 0 2-5.7h3.7a8 8 0 0 1-5.7 5.7z"/></svg>
        www.wardcompass-example.com
      </li>
    </ul>

    <div class="rule"></div>
    <div class="band"></div>
  </section>
</main>
</body>
</html>
```